Harborline Cremations Business Cards

To create a business card for my company Harborline Cremations. Remember it is a cremation company.
We want to make sure people have a business card and information. Something modern, professional
100% Online
Prices starting at $695 all-inclusive (prices subject to change without notice).
A business card is the first point of contact with the prospective client.

Contact Information for Business Card

(305) 418-7260
www.HarborlineCremationsMiami.example
harborlinecremations@mailbox.example

Requirements
Must have
• 100% Online
Prices starting at $695 all-inclusive (prices subject to change without notice)

(305) 418-7260

Must match logo style
Should not have
• No black backgrounds. Please only use the white, orange and blue from the logo

```html
<!DOCTYPE html>
<html lang="en">
<head>
<meta charset="utf-8">
<title>Harborline Cremations Business Cards</title>
<link rel="stylesheet" href="https://fonts.googleapis.com/css2?family=Montserrat:wght@600&family=Ubuntu:wght@400;500;700&display=swap">
<style>
  :root {
    --backdrop: #e6ebef;
    --card: #ffffff;
    --orange: #f07a32;
    --blue: #1a9ee0;
  }
  * { box-sizing: border-box; margin: 0; padding: 0; }
  html, body { width: 1200px; height: 1200px; overflow: hidden; }
  body {
    background: var(--backdrop);
    font-family: "Ubuntu", sans-serif;
    display: flex;
    flex-direction: column;
    align-items: center;
    justify-content: center;
    gap: 60px;
  }
  .card {
    position: relative;
    width: 880px;
    height: 500px;
    background: var(--card);
    border-radius: 28px;
    box-shadow: 0 14px 34px rgba(26, 60, 90, .18);
  }
  /* back side */
  .brand-mark {
    position: absolute;
    left: 50%;
    top: 70px;
    width: 220px;
    height: 220px;
    transform: translateX(-50%);
    border-radius: 50%;
    background: var(--orange);
  }
  .back-tagline {
    position: absolute;
    left: 70px; right: 70px; top: 318px;
    display: flex; align-items: center; gap: 22px;
  }
  .back-tagline .rule { flex: 1; height: 2px; background: var(--blue); }
  .back-tagline .online {
    color: var(--blue); font-weight: 700; font-size: 26px; letter-spacing: .5px;
  }
  .pricing {
    position: absolute;
    left: 0; right: 0; top: 372px;
    text-align: center;
    color: var(--orange);
    font-size: 25px; font-weight: 500;
  }
  .pricing .note { font-weight: 400; font-size: 20px; }
  /* front side */
  .company {
    position: absolute;
    top: 70px; left: 0; right: 0;
    display: flex; align-items: center; justify-content: center; gap: 26px;
  }
  .company .dot {
    width: 110px; height: 110px; border-radius: 50%;
    background: var(--orange);
  }
  .company .name {
    font-family: "Montserrat", sans-serif;
    font-weight: 600;
    color: var(--blue);
    font-size: 40px;
    letter-spacing: 3px;
    line-height: 1.15;
    text-transform: uppercase;
  }
  .details {
    position: absolute;
    top: 290px; left: 0; right: 0;
    display: flex; justify-content: center; align-items: center; gap: 30px;
  }
  .person { text-align: right; }
  .person .full-name { color: var(--orange); font-weight: 700; font-size: 32px; letter-spacing: .5px; }
  .person .role { color: var(--blue); font-size: 22px; margin-top: 4px; }
  .divider { width: 2px; height: 120px; background: var(--blue); }
  .contact { list-style: none; display: flex; flex-direction: column; gap: 10px; }
  .contact li { display: flex; align-items: center; gap: 12px; color: var(--blue); font-size: 20px; white-space: nowrap; }
  .contact svg { width: 20px; height: 20px; flex: none; }
</style>
</head>
<body>

  <section class="card card--back" aria-label="Card back">
    <div class="brand-mark" role="img" aria-label="Harborline Cremations emblem area"></div>
    <div class="back-tagline">
      <span class="rule"></span>
      <span class="online">100% ONLINE</span>
      <span class="rule"></span>
    </div>
    <p class="pricing">Prices starting at $695 all-inclusive <span class="note">(prices subject to change without notice)</span></p>
  </section>

  <section class="card card--front" aria-label="Card front">
    <div class="company">
      <span class="dot"></span>
      <span class="name">Harborline<br>Cremations</span>
    </div>
    <div class="details">
      <div class="person">
        <p class="full-name">DANA WHITLOCK</p>
        <p class="role">Account Executive</p>
      </div>
      <span class="divider"></span>
      <ul class="contact">
        <li>
          <svg viewBox="0 0 24 24"><path fill="#f07a32" d="M6.6 10.8a15.1 15.1 0 0 0 6.6 6.6l2.2-2.2a1 1 0 0 1 1-.25 11.4 11.4 0 0 0 3.6.57 1 1 0 0 1 1 1V20a1 1 0 0 1-1 1A17 17 0 0 1 3 4a1 1 0 0 1 1-1h3.5a1 1 0 0 1 1 1c0 1.25.2 2.45.57 3.6a1 1 0 0 1-.25 1z"/></svg>
          (305) 418-7260
        </li>
        <li>
          <svg viewBox="0 0 24 24"><rect x="2" y="5" width="20" height="14" rx="2" fill="#f07a32"/><path d="M3 6l9 7 9-7" fill="none" stroke="#ffffff" stroke-width="2"/></svg>
          harborlinecremations@mailbox.example
        </li>
        <li>
          <svg viewBox="0 0 24 24"><circle cx="12" cy="12" r="9" fill="none" stroke="#f07a32" stroke-width="2"/><ellipse cx="12" cy="12" rx="4" ry="9" fill="none" stroke="#f07a32" stroke-width="2"/><path d="M3 12h18" stroke="#f07a32" stroke-width="2"/></svg>
          www.HarborlineCremationsMiami.example
        </li>
      </ul>
    </div>
  </section>

</body>
</html>
```